依頼概要
京都一乗寺の老舗ラーメン店『宝楽』の『のぼり』デザインのご提案をお願い致します。

今春に本システムで新しいロゴ作成を依頼し、素晴らしいデザインをご提案頂き、夏前に店舗のリニューアルを行いました。

老舗の本店としての風格を持つファザードに生まれ変わり、次は店前(3本程)と専用駐車場(15本程)にのぼりを設置しようと考えます。

現在のファザードと調和するデザインで、一度入って見たくなるような、新規客の期待感をくすぐる秀作をお待ちしております。

店舗情報は
www.horaku-soba.jp
でご確認下さい。

※ファザードは店舗情報ページに掲載しております。
※味めぐり めしたびもご参照下さい。
※トップページの能書き『見た目こってり...』の筆文字も同時募集いたします。

なお『ラーメン』では無く『中華そば』の表記でお願いします。

■ 依頼の目的/概要
・車両及び歩行客への訴求と認知の向上
・新規客の誘客トリガー
・ファザードと一体となったオリジナリティーのある雰囲気造り

■ 重視する点/検討基準
・文字は『中華そば』『宝楽』が必須
・『創業半世紀』『白川本店』はデザイン次第で採用
・ラーメン店らしい迫力や躍動感

複数のご依頼がございましたラーメン画像をUPします。
容量に制限がございますので、確定次第、元データは直接ご送付致します。
ロゴデータをUP致します。
依頼金額を44000円に変更して、延長しました。
この度は多数のご提案、誠に有難うございました。
折角ではございますが、私の説明不足もあろうかと思いますので追記の上、延長させていただきます。

■店舗ファザードとの統一感を出すため白地へのデザインでお願いします。
(デザイン次第ではこの限りではありませんので、決定時にはご了承下さい)
■「ラーメン・らーめん」では無く「中華そば」で表現下さい。
■「ラーメン画像」は写りも良くないので使用しないで下さい。
■基本的に「中華そば」の文字と「宝楽」のロゴ文字&紋様で構成下さい。
■前述、「宝楽」より「中華そば」を大きくデフォルメ下さい。
■ショルダーは「創業半世紀」「京都 白川本店」以外は不要です。
■色目は3色ぐらいまでを基本とします(黒・赤・紋様の色目)
■前述、グラデーションによって色調が増えるのはOKです。

注文が多く申し訳ございませんが、延長での決定を確実にしたいので、ご海容下さい。

紋様の使い方やグラデーションの背景(筆で描いた躍動感を演出するラインetc..)がポイントになるのでしょうか?

宜しくお願いします。
★(再)ラーメン画像は不要です。宜しくお願いします。★
新しい能書きデザインをUP致します。
本コンペと同時に行ったもので、私どもの趣向の参考にしてください。
★★★ラーメンの絵は不要です★★★

効果的な訴求ですが、製作コストが高く付きます。
■ 選んだ理由

シンプルでメッセージが伝わりやすく、店舗ファザードとも調和の取れたデザインであり、3色(2色でも可能)なので製作コストも軽減できるため。

■ 提案者全員のお礼・コメント

この度はご多数のご提案、誠に有難うございました。
秀作ぞろいで随分悩み、確定まで時間が掛かってしまい恐縮です。
これからも宜しくお願いいたします。

```html
<!DOCTYPE html>
<html lang="ja">
<head>
<meta charset="utf-8">
<title>宝楽 のぼり 中華そば</title>
<link rel="stylesheet" href="https://fonts.googleapis.com/css2?family=Yuji+Boku&family=Zen+Old+Mincho:wght@700;900&display=swap">
<style>
  :root {
    --ink: #111111;
    --paper: #ffffff;
    --stage: #000000;
    --emblem: #c9a58a;
    --pink-top: #f6d3d3;
    --pink-bottom: #e88c8c;
    --red-top: #f7b9b9;
    --red-bottom: #e0302f;
  }
  * { margin: 0; padding: 0; box-sizing: border-box; }
  html, body { width: 849px; height: 1200px; overflow: hidden; background: var(--stage); }
  .canvas { position: relative; width: 849px; height: 1200px; background: var(--stage); }
  .nobori {
    position: absolute; top: 62px; width: 325px; height: 740px;
    background: var(--paper); overflow: hidden;
  }
  .nobori--soft { left: 57px; }
  .nobori--bold { left: 446px; }
  .shoulder {
    position: absolute; top: 0; left: 0; width: 100%; height: 184px;
    text-align: center; color: var(--ink);
    font-family: "Zen Old Mincho", serif;
  }
  .shoulder__tag { position: absolute; top: 12px; width: 100%; font-size: 14px; font-weight: 700; letter-spacing: 2px; }
  .shoulder__name {
    position: absolute; top: 38px; width: 100%;
    display: flex; justify-content: center; align-items: center; gap: 10px;
    font-size: 60px; font-weight: 900; line-height: 1;
  }
  .shoulder__mark { width: 78px; height: 78px; border-radius: 50%; background: var(--emblem); }
  .shoulder__branch { position: absolute; top: 155px; width: 100%; font-size: 12px; font-weight: 700; letter-spacing: 3px; }
  .field { position: absolute; top: 184px; left: 0; width: 100%; height: 556px; }
  .nobori--soft .field { background: linear-gradient(to bottom, var(--pink-top), var(--pink-bottom)); }
  .nobori--bold .field { background: linear-gradient(to bottom, var(--red-top), var(--red-bottom)); }
  .headline {
    position: absolute; top: 196px; left: 0; width: 100%; height: 540px;
    display: flex; justify-content: center;
  }
  .headline__text {
    writing-mode: vertical-rl; text-orientation: upright;
    font-family: "Yuji Boku", serif; font-size: 124px; line-height: 1;
    letter-spacing: 6px; color: var(--ink);
    transform: scaleX(1.5);
    -webkit-text-stroke: 2px var(--ink);
    text-shadow: 0 0 6px rgba(255,255,255,0.9);
  }
</style>
</head>
<body>
<main class="canvas">
  <section class="nobori nobori--soft">
    <header class="shoulder">
      <p class="shoulder__tag">中華そば</p>
      <p class="shoulder__name"><span>宝</span><span class="shoulder__mark" role="img" aria-label="店の紋様"></span><span>楽</span></p>
      <p class="shoulder__branch">白川本店</p>
    </header>
    <div class="field" role="img" aria-label="淡い赤の水玉模様の背景"></div>
    <div class="headline"><h1 class="headline__text">中華そば</h1></div>
  </section>
  <section class="nobori nobori--bold">
    <header class="shoulder">
      <p class="shoulder__tag">中華そば</p>
      <p class="shoulder__name"><span>宝</span><span class="shoulder__mark" role="img" aria-label="店の紋様"></span><span>楽</span></p>
      <p class="shoulder__branch">白川本店</p>
    </header>
    <div class="field" role="img" aria-label="赤い水玉模様の背景"></div>
    <div class="headline"><h1 class="headline__text">中華そば</h1></div>
  </section>
</main>
</body>
</html>
```